Crib Caller

This is a single-page full-screen tablet app that generates baby names based on a few user-selected options. The code is already written; I just need the visual design.
UI elements are:
1) Options, containing:
i) Gender selector
ii) Multi-select
inspiration sources (names based on country of origin)
iii) Scroll speed selector
2) Favourites panel containing list of current favourites (with UI to delete items)
3) Output panel; a live scrolling list of generated names - click to add as a favourite.
The app is a Windows 8 Metro application, written in XAML. It should stick to the Metro conventions/spirit. Here are some docs/samples:
http://docs.quellarion.com/library/tiles/apps/kq552918/
http://en.plexoverum.org/wiki/Lattice_(design_language)
Ideally, design will be presented in XAML format.
The attached design is the crap I've got meanwhile - it shows the basic elements. The list of generated names appears in the white-space on the right. The bar on the bottom is an advertisement.
More on the Metro design principles that should be adhered to:
http://www.quellarion.com/design/toolbox/tutorials/tiles-handset-4/lattice/
Ideal submission would be in XAML format. However, Adobe Illustrator files are decent as well; vector format is important.
Pixel-based images aren't ideal in this case, because Metro applications need to be scalable to any resolution.
Target Market(s)
People expecting a baby; mostly women.
Industry/Entity Type
Baby
Look and feel
Each slider illustrates characteristics of the customer's brand and the style your logo design should communicate.

```html
<!DOCTYPE html>
<html lang="en">
<head>
<meta charset="utf-8">
<title>Crib Caller</title>
<link rel="stylesheet" href="https://fonts.googleapis.com/css2?family=Great+Vibes&family=Open+Sans:wght@400;600;700&display=swap">
<style>
  :root {
    --title-gold: #f7d54a;
    --tile-home: rgba(244, 178, 0, 0.88);
    --tile-favourite: rgba(26, 200, 230, 0.85);
    --tile-gender: rgba(104, 190, 24, 0.9);
    --tile-sun: rgba(246, 196, 0, 0.9);
    --tile-settings: rgba(22, 140, 214, 0.88);
    --tile-meadow: rgba(40, 190, 22, 0.88);
    --tile-linen: rgba(236, 228, 208, 0.85);
    --tile-lagoon: rgba(0, 206, 232, 0.9);
    --tile-ember: rgba(206, 78, 8, 0.9);
    --tile-label: #1c1c1c;
    --icon-ink: rgba(20, 20, 20, 0.62);
    --nav-disc: rgba(60, 60, 60, 0.55);
    --nav-arrow: rgba(150, 150, 150, 0.85);
    --ad-deep: #233a86;
    --ad-light: #3e60b8;
    --ad-gold: #f4c431;
    --ad-orange: #f59a1a;
    --ad-red: #d8262a;
    --ad-text: #ffffff;
  }
  * { box-sizing: border-box; margin: 0; padding: 0; }
  html, body { width: 1200px; height: 720px; overflow: hidden; background: #000; }
  body { font-family: "Open Sans", sans-serif; }

  .app-screen { position: relative; width: 1200px; height: 720px; overflow: hidden; }

  .backdrop-photo {
    position: absolute; inset: 0;
    background:
      radial-gradient(ellipse 150px 170px at 590px 150px, rgba(230, 60, 130, 0.9), transparent 70%),
      radial-gradient(ellipse 200px 260px at 600px 560px, rgba(50, 42, 38, 0.95), transparent 75%),
      radial-gradient(ellipse 220px 220px at 1060px 560px, rgba(228, 120, 30, 0.9), transparent 70%),
      radial-gradient(ellipse 260px 200px at 1050px 160px, rgba(40, 110, 150, 0.7), transparent 70%),
      radial-gradient(ellipse 300px 260px at 120px 620px, rgba(210, 150, 60, 0.7), transparent 70%),
      linear-gradient(100deg, #8aa83a 0%, #6e9a34 30%, #85734a 55%, #7a8a4c 75%, #b47a2c 100%);
  }

  .app-title {
    position: absolute; left: 830px; top: 90px;
    font-family: "Great Vibes", cursive; font-size: 64px; line-height: 1;
    color: var(--title-gold); font-weight: 400;
  }

  .tile-board {
    position: absolute; left: 166px; top: 181px; width: 874px; height: 310px;
    display: grid;
    grid-template-columns: repeat(6, 1fr);
    grid-template-rows: 154px 156px;
  }
  .tile { position: relative; display: flex; align-items: center; justify-content: center; }
  .tile--wide { grid-column: span 2; }
  .tile svg { width: 78px; height: 78px; fill: var(--icon-ink); }
  .tile--small svg { width: 62px; height: 62px; }
  .tile-label {
    position: absolute; right: 6px; bottom: 5px;
    font-size: 16px; color: var(--tile-label);
  }
  .tile-home { background: var(--tile-home); }
  .tile-favourite { background: var(--tile-favourite); }
  .tile-gender { background: var(--tile-gender); }
  .tile-sun { background: var(--tile-sun); }
  .tile-settings { background: var(--tile-settings); }
  .tile-meadow { background: var(--tile-meadow); }
  .tile-linen { background: var(--tile-linen); }
  .tile-lagoon { background: var(--tile-lagoon); }
  .tile-ember { background: var(--tile-ember); }

  .pager-button {
    position: absolute; top: 327px; width: 68px; height: 68px; border-radius: 50%;
    background: var(--nav-disc); display: flex; align-items: center; justify-content: center;
  }
  .pager-button svg { width: 30px; height: 30px; stroke: var(--nav-arrow); stroke-width: 6; fill: none; stroke-linecap: round; stroke-linejoin: round; }
  .pager-button--prev { left: 46px; }
  .pager-button--next { left: 1076px; }

  .ad-banner {
    position: absolute; left: 282px; top: 615px; width: 621px; height: 85px;
    background: linear-gradient(180deg, var(--ad-light), var(--ad-deep));
    overflow: hidden;
  }
  .ad-mark {
    position: absolute; left: 14px; top: 8px; width: 80px; height: 80px;
    background: #6a8be0; border-radius: 8px;
  }
  .ad-name {
    position: absolute; left: 155px; top: 2px;
    font-size: 32px; font-weight: 400; color: var(--ad-text); line-height: 1.2;
  }
  .ad-tagline {
    position: absolute; left: 158px; top: 43px;
    font-size: 14px; font-weight: 600; color: var(--ad-gold);
  }
  .ad-pitch {
    position: absolute; left: 158px; top: 62px;
    display: flex; align-items: center; gap: 8px;
    font-size: 13px; font-weight: 600; color: var(--ad-text);
  }
  .ad-pitch-bullet {
    width: 15px; height: 15px; border-radius: 50%; background: var(--ad-red);
    display: flex; align-items: center; justify-content: center;
  }
  .ad-pitch-bullet svg { width: 9px; height: 9px; fill: #fff; }
  .ad-badge {
    position: absolute; left: 450px; top: 0; width: 130px; height: 38px;
    background: var(--ad-orange); border-radius: 0 0 18px 18px;
    display: flex; align-items: center; justify-content: center;
    font-size: 24px; font-weight: 700; color: var(--ad-text);
  }
</style>
</head>
<body>
<main class="app-screen">
  <div class="backdrop-photo" role="img" aria-label="Soft-focus autumn photo of a toddler in a pink striped knitted hat and scarf holding orange leaves"></div>

  <h1 class="app-title">Crib Caller</h1>

  <button class="pager-button pager-button--prev" aria-label="Previous" style="border:0">
    <svg viewBox="0 0 30 30"><polyline points="19,5 9,15 19,25"/></svg>
  </button>
  <button class="pager-button pager-button--next" aria-label="Next" style="border:0">
    <svg viewBox="0 0 30 30"><polyline points="11,5 21,15 11,25"/></svg>
  </button>

  <nav class="tile-board">
    <div class="tile tile--wide tile-home">
      <svg viewBox="0 0 64 64"><path d="M32 6 2 32l4 4 4-3.5V58h18V42h8v16h18V32.5l4 3.5 4-4L48 18V8h-7v4zM14 29 32 13l18 16v25H40V38H24v16H14z"/><path d="M16 30 32 16l16 14v26H38V40H26v16H16z"/></svg>
      <span class="tile-label">Home</span>
    </div>
    <div class="tile tile--wide tile-favourite">
      <svg viewBox="0 0 64 64"><path d="M32 56 8 32C1 25 2 13 11 9c7-3 15 0 21 8 6-8 14-11 21-8 9 4 10 16 3 23z"/></svg>
      <span class="tile-label">Favourite</span>
    </div>
    <div class="tile tile--wide tile-gender">
      <svg viewBox="0 0 64 64"><path d="M32 4a4 4 0 1 1 0 8 4 4 0 0 1 0-8zM10 34C10 20 20 12 32 12s22 8 22 22zM8 36h48v6H8z"/><path d="M13 44h38c-2 9-10 16-19 16s-17-7-19-16z" fill-opacity="0.5"/></svg>
      <span class="tile-label">Gender</span>
    </div>

    <div class="tile tile--small tile-sun">
      <svg viewBox="0 0 64 64"><path d="M18 48a10 10 0 0 1-1-20 15 15 0 0 1 29-3 11 11 0 0 1 2 23z"/></svg>
    </div>
    <div class="tile tile--small tile-settings">
      <svg viewBox="0 0 64 64"><path d="M6 10h52v40H6zm4 4v32h44V14z"/><path d="M32 20l3 1 1 3 3 1 2-2 3 3-2 2 1 3 3 1v4l-3 1-1 3 2 2-3 3-2-2-3 1-1 3h-4l-1-3-3-1-2 2-3-3 2-2-1-3-3-1v-4l3-1 1-3-2-2 3-3 2 2 3-1 1-3zm0 9a4 4 0 1 0 0 8 4 4 0 0 0 0-8z"/></svg>
      <span class="tile-label">Settings</span>
    </div>
    <div class="tile tile--small tile-meadow">
      <svg viewBox="0 0 64 64"><path d="M18 48a10 10 0 0 1-1-20 15 15 0 0 1 29-3 11 11 0 0 1 2 23z"/></svg>
    </div>
    <div class="tile tile--small tile-linen">
      <svg viewBox="0 0 64 64"><path d="M20 8h3v50h-3z"/><path d="M23 10c10-4 18 6 30 2l-6 12 8 10c-12 4-20-6-32-2z"/></svg>
      <span class="tile-label">Inspiration</span>
    </div>
    <div class="tile tile--small tile-lagoon">
      <svg viewBox="0 0 64 64"><path d="M18 48a10 10 0 0 1-1-20 15 15 0 0 1 29-3 11 11 0 0 1 2 23z"/></svg>
    </div>
    <div class="tile tile--small tile-ember">
      <svg viewBox="0 0 64 64"><path d="M18 48a10 10 0 0 1-1-20 15 15 0 0 1 29-3 11 11 0 0 1 2 23z"/></svg>
    </div>
  </nav>

  <aside class="ad-banner" aria-label="Advertisement">
    <div class="ad-mark"></div>
    <p class="ad-name">GlyphForge 6</p>
    <p class="ad-tagline">The Professional Icon Authoring Tool</p>
    <p class="ad-pitch">
      <span class="ad-pitch-bullet"><svg viewBox="0 0 10 10"><path d="M1 4h4V1l4 4-4 4V6H1z"/></svg></span>
      Easily create Vantor Desk &amp; Pomelo OS icons
    </p>
    <div class="ad-badge">NEW!</div>
  </aside>
</main>
</body>
</html>
```